Bright Vessel, Accelerator for Healthcare Startups, Grand Opening

Bright Vessel is an accelerator for healthcare startup businesses located in North Chicago, Illinois, USA. On July 16th, 4:30 - 6:30 pm, we are having a Grand Opening of our new location, which is at 2417 Calloway, North Chicago, IL. There will be many local dignitaries in attendance, but most importantly we will be unveiling the healthcare startup businesses that will be in our next cohort. We also have four sponsors, logos attached. Here's our website: http://brightvessel.example/

Target Market(s)

Investors, Healthcare Professionals, Politicians, Dignitaries

Industry/Entity Type

Healthcare

Requirements
Must have
• Logo, Date, Time, Location, Sponsors.
Nice to have
• Extremely elegant, professional design.
Should not have
• This is NOT and opening for retail. This is very professional.

```html
<!DOCTYPE html>
<html lang="en">
<head>
<meta charset="utf-8">
<title>Bright Vessel Grand Opening</title>
<link rel="stylesheet" href="https://fonts.googleapis.com/css2?family=Kaushan+Script&family=Pinyon+Script&display=swap">
<style>
  :root {
    --page-edge: #ffffff;
    --parchment: #e9dba9;
    --label-ink: #2a1d17;
    --detail-ink: #8a4b3b;
    --panel-white: #ffffff;
    --sponsor-ink: #2a1d17;
  }
  * { margin: 0; padding: 0; box-sizing: border-box; }
  html, body {
    width: 800px; height: 1200px; overflow: hidden;
    background: var(--page-edge);
  }
  .invitation {
    position: relative;
    width: 800px; height: 1200px;
    overflow: hidden;
    background: var(--page-edge);
  }
  .parchment {
    position: absolute;
    left: 16px; top: 0;
    width: 771px; height: 1200px;
    background: var(--parchment);
  }

  .host {
    position: absolute;
    left: 16px; width: 771px; top: 48px;
    display: flex; align-items: center; justify-content: center; gap: 14px;
    font-family: "Kaushan Script", cursive;
    font-size: 40px;
    color: var(--label-ink);
    line-height: 1;
  }
  .host .mark {
    width: 18px; height: 18px; border-radius: 50%;
    background: var(--label-ink);
  }
  .event-title {
    position: absolute;
    left: 16px; width: 771px; top: 108px;
    text-align: center;
    font-family: "Pinyon Script", cursive;
    font-size: 62px;
    color: var(--detail-ink);
    line-height: 1;
  }

  .label {
    position: absolute;
    font-family: "Kaushan Script", cursive;
    font-size: 42px;
    color: var(--label-ink);
    line-height: 1;
    transform: translateY(-50%);
  }
  .label-date { left: 32px; top: 267px; }
  .label-time { left: 29px; top: 473px; }
  .label-venue { left: 20px; top: 620px; }
  .label-email { left: 20px; top: 911px; }

  .detail {
    position: absolute;
    left: 160px; width: 640px;
    text-align: center;
    font-family: "Pinyon Script", cursive;
    color: var(--detail-ink);
    line-height: 1;
    transform: translateY(-50%);
  }
  .detail-date { top: 272px; font-size: 72px; }
  .detail-time { top: 473px; font-size: 60px; }
  .detail-venue { font-size: 46px; }
  .detail-venue.line-1 { top: 611px; }
  .detail-venue.line-2 { top: 673px; }
  .detail-venue.line-3 { top: 764px; }
  .detail-web { top: 911px; font-size: 58px; }

  .sponsor {
    position: absolute;
    display: flex; align-items: center; justify-content: center;
    font-family: "Kaushan Script", cursive;
    color: var(--sponsor-ink);
    line-height: 1;
  }
  .sponsor-hopwise {
    left: 24px; top: 1064px; width: 180px; height: 96px;
    font-size: 30px; gap: 10px;
  }
  .sponsor-hopwise .dot {
    width: 16px; height: 16px; border-radius: 50%;
    background: var(--sponsor-ink);
  }
  .sponsor-roast {
    left: 210px; top: 1090px; width: 228px; height: 70px;
    font-size: 22px;
  }
  .sponsor-ember {
    left: 460px; top: 1049px; width: 120px; height: 130px;
    background: var(--panel-white);
    font-size: 24px; text-align: center;
  }
  .sponsor-sugarline {
    left: 611px; top: 1027px; width: 172px; height: 153px;
    background: var(--panel-white);
    font-size: 32px;
  }
</style>
</head>
<body>
<main class="invitation">
  <div class="parchment"></div>

  <header>
    <p class="host"><span class="mark"></span>Bright Vessel</p>
    <h1 class="event-title">Grand Opening</h1>
  </header>

  <p class="label label-date">Date-</p>
  <p class="detail detail-date">July16th, 2015.</p>

  <p class="label label-time">Time-</p>
  <p class="detail detail-time">4:30-6:30p.m</p>

  <p class="label label-venue">Venue-</p>
  <p class="detail detail-venue line-1">North Chicago Illinois. U.S.A</p>
  <p class="detail detail-venue line-2">2417 Calloway,</p>
  <p class="detail detail-venue line-3">North Chicago, IL</p>

  <p class="label label-email">Email-</p>
  <p class="detail detail-web">www.brightvessel.example</p>

  <section class="sponsors" aria-label="Sponsors">
    <div class="sponsor sponsor-hopwise"><span class="dot"></span>Hopwise</div>
    <div class="sponsor sponsor-roast">roastandmill.example</div>
    <div class="sponsor sponsor-ember">Ember<br>Kitchen</div>
    <div class="sponsor sponsor-sugarline">Sugarline</div>
  </section>
</main>
</body>
</html>
```